Consumer Credit Attorney Needs Logo for Letterhead & Business cards

I need a basic logo or letterhead design for a new law firm in Mobile, Alabama. The firm is called "Harlow T. Benning, PC." We represent people fighting large corporations in cases involving Fair Credit Reporting, Debt Collection, Mortgage Fraud, Truth in Lending, and Wrongful Foreclosures. I don't want anything with scales of justice or columns or the typical lawyer imagery. I ride a bike to court. I keep most of my office in the cloud. I'm a different type of lawyer, and I want a design that is simple, elegant, and made primarily of blue and white.
Updates

The Job is now Payment Committed.  I look forward to seeing your submissions.  Thanks1

Project Deadline Extended
Reason: I have just recently received some new designs and provided feedback on them. You all deserve some time to consider the feedback. Thanks!

Industry/Entity Type

Business

Requirements
Nice to have
• Clear lines and a small footprint on the letterhead. I like several antique styles- Gilded Age, Rococo, Edwardian, even Art Deco.
Should not have
• The only thing I hate is 1990s clip-art style graphics. No illustrations of money, courthouses, scales, columns, etc. I also hate silly fonts, overly fancy or "handwritten" fonts, and Arial font.

```html
<!DOCTYPE html>
<html lang="en">
<head>
<meta charset="utf-8">
<title>Harlow T. Benning, PC — Stationery</title>
<link rel="stylesheet" href="https://fonts.googleapis.com/css2?family=Cormorant+Garamond:ital,wght@0,500;0,600;1,500&display=swap">
<style>
  :root {
    --backdrop: #d0d0d0;
    --paper: #ffffff;
    --navy: #2e3192;
    --ink: #1f2388;
    --on-navy: #ffffff;
  }
  * { margin: 0; padding: 0; box-sizing: border-box; }
  html, body {
    width: 1200px;
    height: 1000px;
    overflow: hidden;
    background: var(--backdrop);
  }
  .canvas {
    position: relative;
    width: 1200px;
    height: 1000px;
    font-family: "Cormorant Garamond", Georgia, serif;
  }

  /* Shared brand block */
  .brand {
    position: absolute;
    left: 0;
    right: 0;
    display: flex;
    flex-direction: column;
    align-items: center;
  }
  .brand-dot {
    width: 34px;
    height: 34px;
    border-radius: 50%;
    background: var(--navy);
  }
  .brand-name {
    color: var(--ink);
    font-weight: 600;
    font-variant: small-caps;
    letter-spacing: 0.03em;
    white-space: nowrap;
  }

  /* Note card */
  .note-card {
    position: absolute;
    left: 30px;
    top: 575px;
    width: 400px;
    height: 330px;
    background: var(--paper);
  }
  .note-card .brand { top: 66px; }
  .note-card .brand-name { font-size: 17px; margin-top: 22px; }
  .note-card__band {
    position: absolute;
    left: 0;
    right: 0;
    bottom: 0;
    height: 98px;
    background: var(--navy);
    display: flex;
    align-items: center;
    justify-content: center;
  }
  .note-card__greeting {
    color: var(--on-navy);
    font-style: italic;
    font-weight: 500;
    font-size: 20px;
    letter-spacing: 0.3em;
  }

  /* Letterhead */
  .letterhead {
    position: absolute;
    left: 468px;
    top: 48px;
    width: 688px;
    height: 896px;
    background: var(--paper);
  }
  .letterhead__band {
    height: 18px;
    background: var(--navy);
  }
  .letterhead .brand { top: 64px; }
  .letterhead .brand-name { font-size: 18px; margin-top: 26px; }
  .letterhead__footer {
    position: absolute;
    left: 0;
    right: 0;
    bottom: 32px;
    text-align: center;
    color: var(--ink);
    font-weight: 600;
    font-size: 11px;
    font-variant: small-caps;
    letter-spacing: 0.02em;
    white-space: nowrap;
  }
</style>
</head>
<body>
<main class="canvas">

  <section class="note-card" aria-label="Thank-you note card">
    <div class="brand">
      <div class="brand-dot"></div>
      <p class="brand-name">Harlow T. Benning, PC</p>
    </div>
    <div class="note-card__band">
      <p class="note-card__greeting">Thank You</p>
    </div>
  </section>

  <section class="letterhead" aria-label="Letterhead">
    <div class="letterhead__band"></div>
    <div class="brand">
      <div class="brand-dot"></div>
      <p class="brand-name">Harlow T. Benning, PC</p>
    </div>
    <p class="letterhead__footer">418 Harbor Street, Mobile, Alabama 36602, PO Box 5142, Daphne, Alabama 36526, Telephone: 251.555.0173</p>
  </section>

</main>
</body>
</html>
```